Website design for Cambridge based systematic hedge fund

We have run previous craftmosaic competitions to design our company logo, business cards and the styling of our presentation deck (see attached files).
As the final step we are looking to get a website designed that is thematically consistent with these existing elements of our branding.
You can find some of our competitors websites below:
https://www.quelmarsh.example/
https://www.fenloor.example/
https://www.pyvart.example/
https://www.dulvet.example/
https://www.orbelmfunds.example/
https://www.valtrigo.example/
https://www.meskilfunds.example/home
We would like to have a website that works well on both mobile devices and desktops. Either just as one page that can be scrolled down, with links at the top that skips to certain sections, or a few separate pages that can be navigated by a top menu.
It should look professional, we are not after lots of animations or unnecessary transitions, and in particular the website must be smooth to navigate. We would like to avoid having peoples of people, we are happy to make use of elements from the presentation (for example the style of the cover slide, or the section slides with the faded bridge in the background), or 'financial' style images.
We would like to have the following sections for now. For some of these some example text has been provided, final text may change but it will be of similar length. For the other sections we are happy to just have template text for now. At the moment we are mainly interested to see styles/layouts as words can be added easily afterwards:
1) We will need a disclaimer pop up the first time someone visits the site (see for example the meskilfunds example).
2) Top page - company name, then in larger text "Bringing AI and Statistical Inference to Financial Markets", and somewhere in smaller text "Harlow Vectors is a quantitative asset manager with the singular focus of delivering algorithmic strategies that work"
3) "About us" section: will describe us as a company, details our approach, company values, and explains the company logo.
Example text:
"We deliver consistent alpha across liquid markets through the application of proprietary IP in Bayesian inference, machine learning and artificial intelligence. We are a multi-disciplinary team founded by experienced finance professionals from premier institutions, leading academics from the Thornbury Stellar Unit at Ashmere College and world-class software engineers.
Our logo portrays a sillhoute of the lattice walkway at Ashmere College. Our unique scientific approach allows us to bridge cutting-edge mathematical research and computing expertise with financial knowledge to bring algorithmns that work to liquid markets"
4) Hiring section, detailing our culture, what we are looking for.
Example text:
"We are always looking for exceptional talent to join our entrepreneurial team. We are looking for individuals who are creative thinkers, can demonstrate analytical rigour and are passionate about the intersection of science, finance and technology.
We prioritise having a company culture that promotes sharing ideas in a safe, collaborative research environment. We make sure that every member of the team has the oppertunity to explore their own ideas through weekly 'innovation time', and ensure that everyone gets the support they need to continue to grow as individuals within the company."
5) A section for news/press releases
6) Contact us area at the bottom with office location and email. We will need to list 3 addresses for our Cambridge, London and Singapore offices, along with a couple of contact emails or phone numbers
7) A client login button at the top that will take them to a different website (unrelated to this one).

```html
<!DOCTYPE html>
<html lang="en">
<head>
<meta charset="utf-8">
<title>Harlow Vectors Asset Management</title>
<link href="https://fonts.googleapis.com/css2?family=Roboto:wght@300;400;500;700&family=Montserrat:wght@400;500;600&display=swap" rel="stylesheet">
<style>
:root{
  --navy:#0c2340;
  --brand:#0a4a7c;
  --link:#0f5a8f;
  --text:#1a1a1a;
  --muted:#606060;
  --paper:#ffffff;
  --soft:#f2f2f2;
  --line:#c9c9c9;
  --btn-grey:#a9a9a9;
}
*{box-sizing:border-box;margin:0;padding:0}
html,body{width:1200px;height:686px;overflow:hidden}
body{position:relative;font-family:'Roboto',sans-serif;background:var(--paper);color:var(--text)}

/* page */
.topbar{position:absolute;left:0;top:0;width:1200px;height:25px;background:#2a3f5c;font-family:'Montserrat',sans-serif;font-size:8.5px;color:#dfe6ee}
.office{position:absolute;left:0;top:0;width:256px;height:25px;background:var(--navy);display:flex;align-items:center;justify-content:flex-end;padding-right:12px;font-size:10px;font-weight:500;letter-spacing:.3px}
.office::after{content:"";border:3px solid transparent;border-top:4px solid #dfe6ee;margin:4px 0 0 6px}
.contact{position:absolute;top:0;height:25px;display:flex;align-items:center;gap:6px}
.contact svg{width:14px;height:14px;fill:none;stroke:#dfe6ee;stroke-width:1.4}
.phone{left:269px}.email{left:372px}
.lang{position:absolute;left:1016px;top:8px;font-size:8px}

.header{position:absolute;left:0;top:25px;width:1200px;height:126px;background:var(--soft);border-bottom:1px solid #3a6ea5}
.social{position:absolute;left:162px;top:44px;display:flex;gap:9px}
.social span{width:25px;height:25px;border:1px solid #444;border-radius:50%}
.site-name{position:absolute;left:530px;top:30px;width:140px;text-align:center;font-family:'Montserrat',sans-serif;font-weight:600;font-size:15px;line-height:17px;color:var(--brand)}
.login{position:absolute;left:919px;top:44px;display:flex;align-items:center;gap:7px;font-family:'Montserrat',sans-serif;font-size:10px;letter-spacing:2px;color:#333}
.login i{width:25px;height:25px;border:1px solid #444;border-radius:50%;display:block;position:relative}
.login i::before{content:"";position:absolute;left:8px;top:5px;width:7px;height:7px;border-radius:50%;background:#333}
.login i::after{content:"";position:absolute;left:5px;top:13px;width:13px;height:7px;border-radius:7px 7px 2px 2px;background:#333}

.hero{position:absolute;left:0;top:152px;width:1200px;height:267px;background:#eef1f5}
.tile{position:absolute;top:419px;height:267px}
.tile-phone{left:0;width:300px;background:linear-gradient(135deg,#5f8fc4,#2c4f7a 60%,#c89a86)}
.tile-mid{left:300px;width:300px;background:linear-gradient(180deg,#e4e7ec,#cfd4db)}
.tile-blank{left:600px;width:300px;background:#ffffff}
.tile-chart{left:900px;width:300px;background:linear-gradient(160deg,#dde7f0,#7fa3c4 55%,#1f4f7e)}

.shade{position:absolute;inset:0;background:rgba(0,0,0,.5)}

/* disclaimer */
.disclaimer{position:absolute;left:268px;top:102px;width:664px;height:482px;background:var(--paper)}
.disclaimer .mark{position:absolute;left:25px;top:36px;font-family:'Montserrat',sans-serif;font-weight:600;font-size:17px;line-height:20px;color:var(--brand)}
.disclaimer h1{position:absolute;left:0;top:84px;width:664px;text-align:center;font-weight:400;font-size:29px;color:var(--brand)}
.intro{position:absolute;left:18px;top:137px;width:632px;font-weight:500;font-size:12.5px;line-height:19px;color:#111}
.intro a,.terms a{color:var(--link);text-decoration:none}
.terms{position:absolute;left:18px;top:214px;width:618px;height:106px;overflow:hidden}
.terms h2{font-size:12px;font-weight:500;color:#111}
.terms p{margin-top:20px;font-size:11.5px;line-height:18.75px;color:var(--muted);font-weight:400;padding-right:6px}
.scrollbar{position:absolute;left:637px;top:218px;width:8px;height:100px}
.scrollbar::before{content:"";position:absolute;left:0;top:10px;width:8px;height:80px;border-radius:4px;background:#f0f0f0}
.scrollbar i{position:absolute;left:0;top:10px;width:8px;height:30px;border-radius:4px;background:#c4c4c4}
.scrollbar b{position:absolute;left:1px;bottom:-2px;border:3px solid transparent;border-top:6px solid #aaa}
.actions{position:absolute;left:201px;top:339px;display:flex;gap:9px}
.actions button{height:34px;border:0;font-family:'Montserrat',sans-serif;font-weight:500;font-size:10.5px;letter-spacing:1.6px;color:#fff}
.accept{width:106px;background:var(--brand)}
.decline{width:148px;background:var(--btn-grey)}
.cookies{position:absolute;left:19px;top:392px;width:627px;height:71px;background:#ececec;border:1px solid var(--line);padding:11px 12px}
.cookies h3{font-size:10px;font-weight:500;color:#111}
.cookies p{margin-top:3px;font-size:10.6px;line-height:17px;color:#333;font-weight:300}
.cookies a{color:var(--link);text-decoration:none;font-weight:400}
</style>
</head>
<body>
<div class="topbar">
  <div class="office">LONDON</div>
  <div class="contact phone"><svg viewBox="0 0 16 16"><path d="M3 2l3 3-1.5 2a8 8 0 004.5 4.5L11 10l3 3-2 2C7 15 1 9 1 4z"/></svg>+44 7700 900123</div>
  <div class="contact email"><svg viewBox="0 0 16 16"><rect x="1" y="3" width="14" height="10"/><path d="M1 3l7 6 7-6"/></svg>info@hvam.example</div>
  <div class="lang">EN ▾</div>
</div>
<header class="header">
  <div class="social" aria-label="Social profiles"><span></span><span></span><span></span></div>
  <div class="site-name">Harlow Vectors</div>
  <div class="login"><i></i>CLIENT LOGIN</div>
</header>
<section class="hero"></section>
<div class="tile tile-phone" role="img" aria-label="Photo of a hand holding a phone showing a candlestick chart"></div>
<div class="tile tile-mid" role="img" aria-label="Faded background image"></div>
<div class="tile tile-blank"></div>
<div class="tile tile-chart" role="img" aria-label="Photo of financial charts on a desk with a pen"></div>
<div class="shade"></div>

<div class="disclaimer" role="dialog" aria-labelledby="dlg-title">
  <div class="mark">Harlow Vectors</div>
  <h1 id="dlg-title">Harlow Vectors Asset Management</h1>
  <p class="intro">Please read these Terms of Use (the “Terms”) carefully before proceeding as they explain certain restrictions imposed by law on the distribution of the information on this website – <a href="#">www.harlowvectors.example</a> - and the investor portal made available therein (the “Website”).</p>
  <div class="terms">
    <h2>1.Harlow Vectors Asset Management</h2>
    <p>1.1 The Website is operated and issued by Harlow Vectors Asset Management (“HVAM” or the “Company”, “we”, or “us”) which is authorised and regulated by the Financial Oversight Board of the United Kingdom (the “FOB”) (Reference Number: 904417). You can gain access to the FOB’s rules and guidance notes from the following link: <a href="#">http://www.fob-register.example</a>.</p>
  </div>
  <div class="scrollbar"><i></i><b></b></div>
  <div class="actions">
    <button class="accept">I ACCEPT</button>
    <button class="decline">I DO NOT ACCEPT</button>
  </div>
  <div class="cookies">
    <h3>COOKIES CONTROL</h3>
    <p>This website uses cookies. By Continuing to use this website you are giving consent to cookies being used. For information on cookies, visit our <a href="#">Cookies Policy</a>.</p>
  </div>
</div>
</body>
</html>
```